Growing Wellness Company Needs an Amazing Cover for a series of Booklets

We are publishing our own series of booklets on health & wellness topics, called Vital Spark Primers and need an inspiring, modern design for the cover. We are beginning with the Title Diabetes: Type 2, but we will use this design for other titles later one.

SIZE:
This will be the front and back of a 8.5 x 5.5 booklet, plus 2 sample interior pages.

COLOR:
We are an industry leaders and prefer touse vibrant colors and designs to inspire our clients to change to a healthier lifestyle.

REQUIREMENTS:
I am attaching our Vital Spark logo, which needs to be on each cover, but does not need to be the focal point. You may you the words vital spark or just the b logo. The topic/title needs to be no lower than 1/2" from the top of the cover.

I'm attaching some samples of items I like, but please be creative!
If you would like to see some of our other in-house samples of publications send me a message and I'll show you. I will give detailed feedback so dive in and get creative!

FRONT COVER: 
1. Can you please make sure the title is in the top 1.5" of the page, i can't tell from this view. 
Type 2 Diabetes (1st line, bigger) 
A Simple Guide to Understanding & Controlling Your Blood Sugar (Second Row, much smaller) this can also be below the 1.5" line if it needs to be. 
3.We would like to see three shapes maybe toward the bottom with these words in them, one word per shape. inspire, equip, succeed 

IMAGE 
1. We would like you to leave a placeholder for an image, but would like to see different shapes, such as a rounded square or rectangle or a rectangle with two square corners and two rounded corners. 
2. Please play with some different border options as well,

BACKSIDE 
1. please put our information on the back side on the bottom, small. the information i will put in a file on the brief, the 2nd page has our address, phone, etc. 
2. Add our TA logo (attached as an image in the design brief)

Thanks! looking forward to what else you have. 

Reason: I want to give more time to get more/better designs in, i know this is a little more involved project.

Reason: Still not happy with designs, would like to see more.

Hello - thank you for submitting designs, the designs are getting a little too busy....here is a website I love the simplicity of...thanks!  http://www.brightmeadowcare.example   

Reason: We are getting closer to narrowing it down, I want to give the designers a few more days to tweak their designs, then i will ask the final 2 or 3 to submit a couple version of the inside pages. I will supply text for those so you know what you're working with. Thanks!

Target Market(s)

Our clients are adults, about 50/50 men & women in the age range from 20-70 with most being in their early 50's. from high school education up to professional degrees

Font styles to use
Serif
Sans Serif
Script

Colors
a64599
e34197
00a98f
9bcb3c
ffc214
f78f20
f37122
0492cd
6a439a

Requirements
Must have
• Eye catching, inspiring design that entices people to read our booklet:

I need a front and back cover and 2 interior page samples , we will be using more of an info graphic style inside possible with a few actual photographs

FRONT COVER REQUIREMENTS:
Title (must be no lower than 1.5" below the top)
Vital Spark Logo (attached in pink and green)
Thrive Allies' Logo

BACK COVER REQUIREMENTS:
a place for summary text
thrive allies contact information
a place for an item # (can be small, no barcode)
Nice to have
• the colors i chose are samples, does not need to include every color, each title we write will have a different color story

I can appreciate a white cover with some amazing art of pops of color, but i would also love a really rich color with subtle tone on tone things (see the navy blue cover picture)
Should not have
• boring colors, lots of pictures, typical booklet design

```html
<!DOCTYPE html>
<html lang="en">
<head>
<meta charset="utf-8">
<title>Type 2 Diabetes – Vital Spark Primers</title>
<link href="https://fonts.googleapis.com/css2?family=Open+Sans:wght@300;400;600;700;800&display=swap" rel="stylesheet">
<style>
  :root {
    --bg: #e9e6ea;
    --purple-light: #8e3aa3;
    --purple: #6f2587;
    --purple-deep: #4f1563;
    --plum: #5a1f6e;
    --teal: #00a98f;
    --green: #9bcb3c;
    --yellow: #ffc214;
    --orange: #f78f20;
    --orange-deep: #f37122;
    --blue: #0492cd;
    --white: #ffffff;
    --ink-soft: rgba(255,255,255,.75);
  }
  * { box-sizing: border-box; margin: 0; padding: 0; }
  html, body { width: 1200px; height: 880px; overflow: hidden; }
  body {
    background: var(--bg);
    font-family: "Open Sans", Arial, sans-serif;
    color: var(--white);
    position: relative;
  }
  .spread {
    position: absolute; left: 60px; top: 205px;
    width: 1080px; height: 470px;
    display: flex;
    box-shadow: 0 12px 30px rgba(0,0,0,.25);
  }
  .page {
    position: relative; width: 540px; height: 470px; overflow: hidden;
    background:
      radial-gradient(circle at 70% 30%, rgba(200,90,210,.35), transparent 60%),
      linear-gradient(135deg, var(--purple-light), var(--purple) 55%, var(--purple-deep));
  }
  .page--back { border-right: 1px solid rgba(0,0,0,.2); }
  .page svg.shapes { position: absolute; inset: 0; }
  .abs { position: absolute; }

  .title {
    font-weight: 800; font-size: 44px; letter-spacing: .5px; line-height: 1;
    text-shadow: 0 2px 4px rgba(0,0,0,.25);
  }
  .back-title { left: 45px; top: 48px; }
  .back-kicker { left: 138px; top: 96px; font-weight: 300; font-size: 14px; letter-spacing: 1px; color: var(--ink-soft); }

  .bubble-head { font-weight: 700; font-size: 15px; }
  .signs { left: 52px; top: 250px; width: 150px; }
  .signs ul { list-style: none; margin-top: 6px; }
  .signs li { font-size: 9.5px; line-height: 15px; padding-left: 14px; position: relative; }
  .signs li::before { content: ""; position: absolute; left: 0; top: 4px; width: 7px; height: 7px; border-radius: 50%; background: var(--white); }
  .stat { left: 155px; top: 342px; width: 100px; text-align: center; }
  .stat small { display: block; font-size: 8.5px; line-height: 10px; }
  .stat strong { display: block; font-size: 34px; font-weight: 800; line-height: 36px; }
  .lifestyle { left: 222px; top: 280px; width: 116px; text-align: center; font-weight: 700; font-size: 14px; line-height: 16px; }
  .lifestyle .amp { display: block; font-size: 30px; font-weight: 800; line-height: 36px; }
  .prevent { left: 330px; top: 318px; width: 100px; text-align: center; font-weight: 800; font-size: 15px; line-height: 17px; }
  .cause { left: 320px; top: 130px; width: 170px; }
  .cause p { font-size: 7.5px; line-height: 10px; margin-top: 4px; }

  .brand { font-weight: 700; font-size: 17px; color: var(--green); display: flex; align-items: center; gap: 6px; }
  .brand::before { content: ""; width: 12px; height: 12px; border-radius: 50%; background: var(--green); }
  .back-brand { left: 30px; bottom: 22px; }
  .contact { left: 150px; bottom: 28px; font-size: 7px; color: var(--ink-soft); }
  .item-no { right: 24px; bottom: 12px; font-size: 7px; color: var(--ink-soft); }
  .partner { display: flex; align-items: center; gap: 6px; }
  .partner .mark { width: 14px; height: 14px; background: var(--white); border-radius: 2px; }
  .partner .name { font-size: 11px; font-weight: 600; line-height: 12px; }
  .partner .tag { font-size: 7px; color: var(--ink-soft); }
  .back-partner { right: 30px; top: 408px; }
  .front-partner { left: 36px; bottom: 28px; }

  .front-title { left: 0; right: 0; top: 52px; text-align: center; font-size: 46px; }
  .front-sub { left: 0; right: 0; top: 106px; text-align: center; font-weight: 300; font-size: 15px; line-height: 19px; }
  .portrait {
    left: 203px; top: 163px; width: 134px; height: 134px; border-radius: 50%;
    border: 5px solid var(--white);
    background: radial-gradient(circle at 50% 40%, #e8e2dc, #b9b2ad 70%, #8d8a92);
  }
  .pillars { left: 0; right: 0; top: 355px; display: flex; justify-content: center; gap: 38px; }
  .pillar { display: flex; align-items: center; gap: 6px; font-size: 15px; font-weight: 400; }
  .pillar svg { width: 14px; height: 14px; }
  .front-brand { right: 30px; bottom: 52px; }
</style>
</head>
<body>
<main class="spread">
  <!-- Back cover -->
  <section class="page page--back">
    <svg class="shapes" viewBox="0 0 540 470" aria-hidden="true">
      <circle cx="190" cy="315" r="120" fill="var(--plum)" opacity=".85"/>
      <circle cx="310" cy="290" r="135" fill="var(--plum)" opacity=".75"/>
      <circle cx="128" cy="300" r="82" fill="var(--teal)"/>
      <circle cx="410" cy="215" r="108" fill="var(--green)"/>
      <circle cx="280" cy="315" r="66" fill="var(--orange)"/>
      <circle cx="380" cy="345" r="58" fill="var(--yellow)"/>
      <circle cx="205" cy="380" r="55" fill="var(--blue)"/>
    </svg>
    <h1 class="abs title back-title">TYPE 2 DIABETES</h1>
    <p class="abs back-kicker">INFORMATION &amp; SUMMARY</p>

    <div class="abs signs">
      <h2 class="bubble-head">Signs &amp; Symptoms</h2>
      <ul>
        <li>polyuria (frequent urination)</li>
        <li>polydipsia (increased thirst)</li>
        <li>polyphagia (increased hunger)</li>
        <li>weight loss</li>
      </ul>
    </div>
    <div class="abs stat"><small>Excess body fat is associated with</small><strong>90%</strong><small>of the cases</small></div>
    <div class="abs lifestyle">Improve your lifestyle<span class="amp">&amp;</span></div>
    <div class="abs prevent">PREVENT DIABETES</div>
    <div class="abs cause">
      <h2 class="bubble-head">Cause</h2>
      <p>Type 2 diabetes develops from a mix of lifestyle and genetic factors. Some, like diet and weight, are within personal control; others, like age, gender and family history, are not. Poor sleep has also been linked to the condition through its effect on metabolism, and a mother's nutrition before birth may play a part as well.</p>
    </div>

    <div class="abs brand back-brand">Vital Spark</div>
    <p class="abs contact">Thrive Allies LLC | 42 Orchard Lane | P.O. Box 210 | Fernvale, NE 68000 | thriveallies.example | 800.555.0142</p>
    <div class="abs partner back-partner">
      <span class="mark"></span>
      <div><div class="name">Thrive Allies</div><div class="tag">Caring, Proven Wellness</div></div>
    </div>
    <p class="abs item-no">Item #VS-0201</p>
  </section>

  <!-- Front cover -->
  <section class="page page--front">
    <svg class="shapes" viewBox="0 0 540 470" aria-hidden="true">
      <circle cx="225" cy="208" r="58" fill="var(--teal)"/>
      <circle cx="292" cy="185" r="56" fill="var(--yellow)"/>
      <circle cx="330" cy="240" r="50" fill="var(--blue)"/>
      <circle cx="272" cy="280" r="46" fill="var(--orange-deep)"/>
      <circle cx="212" cy="262" r="40" fill="var(--green)"/>
    </svg>
    <h1 class="abs title front-title">TYPE 2 DIABETES</h1>
    <p class="abs front-sub">A Simple Guide to Understanding &amp; Controlling Your<br>Blood Sugar</p>
    <div class="abs portrait" role="img" aria-label="Portrait photo of a smiling doctor"></div>

    <div class="abs pillars">
      <span class="pillar">
        <svg viewBox="0 0 14 14" aria-hidden="true"><path d="M7 1 L8.3 5.7 L13 7 L8.3 8.3 L7 13 L5.7 8.3 L1 7 L5.7 5.7 Z" fill="var(--white)"/></svg>inspire
      </span>
      <span class="pillar">
        <svg viewBox="0 0 14 14" aria-hidden="true"><path d="M5 1h4v4h4v4H9v4H5V9H1V5h4z" fill="var(--white)"/></svg>equip
      </span>
      <span class="pillar">
        <svg viewBox="0 0 14 14" aria-hidden="true"><path d="M1.5 7.5 L5.5 11.5 L12.5 2.5" fill="none" stroke="var(--white)" stroke-width="2.6" stroke-linecap="round"/></svg>succeed
      </span>
    </div>

    <div class="abs brand front-brand">Vital Spark</div>
    <div class="abs partner front-partner">
      <span class="mark"></span>
      <div><div class="name">Thrive Allies</div><div class="tag">Caring, Proven Wellness</div></div>
    </div>
  </section>
</main>
</body>
</html>
```